Modern and Clean Web Re-Design Project

We have 2 companies in similar industries: Printing and Mail Preparation/Fulfillment. We prefer sites that are clean and easy to navigate.Our printing company, Harbourline Press Works' website, hpwgroup-example.ca is outdated needs revamping. We have rebranded our logo and are looking for a new design that is clean, modern and geared to other corporations and business in the downtown Toronto area. Our mailing company, The Parcel Loft (theparcelloft-example.ca) needs a website as well. This company is in the Direct Mail and letter shop business, which essentially is addressing/personalizing people's printed matter and preparing it for either the Canadian or US postal service. The Parcel Loft specializes in not-for-profit and corporate sectors.Please see our logos to get an idea of the colors and look we want. For all intensive purposes, the sites can look similar in design all we want is that each site has the appropriate corporate colors and is a bit different so they don't look identical as the two business run as separate corporations.The content of the website should be easily changed by our staff and we want it to be setup to optimized for SEO based on the keywords we want. We are looking for someone to work on this project immediately

After doing some thinking, I would like the site to be more modern but the non flash sites that I have seen so far Im finding life-less and while I want something clean, not overly busy and corporate looking, I dont want the design to be bland looking.

Please design with the previous specs in mind but with a twist as mentioned above.

Thanks
Dorian

Target Market(s)

See above

Industry/Entity Type

Printing

Requirements
Must have
• Must match the design and style of each respective logoSee the attached impage of the front of our offices to have an idea of our lookWe must be able to edit the content ourselves without any fancy programs or tools.Must be SEO optimized
Nice to have
• An online order form that can be emailed to us for quotes.....perhaps a page with a bunch of fields that have drop down menus....
Should not have
• Should not be overly busy. I want it to be clean and simple but informative without being hard to navigate

```html
<!DOCTYPE html>
<html lang="en">
<head>
<meta charset="utf-8">
<title>Harbourline Press Works – Contact Us</title>
<link rel="stylesheet" href="https://fonts.googleapis.com/css2?family=Mulish:wght@400;600&family=Open+Sans:wght@400;600&display=swap">
<style>
  :root {
    --brand-orange: #f05535;
    --nav-orange: #f26a2e;
    --ink: #222222;
    --muted: #444444;
    --required: #c0392b;
    --field-border: #a9bccb;
    --footer-text: #ffffff;
    --dark-panel: #2b2727;
    --mail-green: #7cb342;
    --page: #ffffff;
  }
  * { box-sizing: border-box; margin: 0; padding: 0; }
  html, body { width: 1200px; height: 997px; overflow: hidden; background: var(--page); }
  body { position: relative; font-family: "Mulish", Arial, sans-serif; color: var(--ink); }

  .site-header { position: absolute; left: 0; top: 0; width: 1200px; height: 124px; }
  .brand { position: absolute; left: 48px; top: 52px; display: flex; align-items: center; gap: 10px; }
  .brand-mark { width: 22px; height: 22px; border-radius: 50%; background: var(--brand-orange); }
  .brand-name { font-size: 19px; font-weight: 600; color: var(--brand-orange); letter-spacing: .2px; }
  .contact-line { position: absolute; right: 20px; top: 14px; font-size: 18px; line-height: 23px; color: var(--nav-orange); }
  .main-nav { position: absolute; right: 20px; top: 92px; display: flex; gap: 31px; }
  .main-nav a { font-size: 22px; color: var(--nav-orange); text-decoration: none; }
  .header-band { position: absolute; left: 0; top: 124px; width: 1200px; height: 14px; background: var(--brand-orange); }

  .staff-photo { position: absolute; left: 215px; top: 193px; width: 257px; height: 257px;
    background: linear-gradient(180deg, #c9a77e 0%, #b08a60 35%, #2c3a5e 70%, #222c48 100%); }
  .partner-badge { position: absolute; left: 203px; top: 486px; display: flex; align-items: center; gap: 10px; }
  .partner-mark { width: 26px; height: 26px; background: var(--mail-green); }
  .partner-name { font-size: 24px; font-weight: 600; color: var(--ink); }
  .brand-panel { position: absolute; left: 220px; top: 583px; width: 251px; height: 144px; background: var(--dark-panel);
    display: flex; align-items: center; justify-content: center; gap: 10px; }
  .brand-panel .brand-mark { width: 18px; height: 18px; }
  .brand-panel .brand-name { font-size: 18px; color: #ffffff; }

  .contact-form { position: absolute; left: 556px; top: 198px; width: 340px; font-family: "Open Sans", Verdana, sans-serif; }
  .form-title { font-size: 14px; font-weight: 400; letter-spacing: .4px; color: var(--ink); }
  .privacy-note { margin-top: 6px; font-size: 10.5px; line-height: 14.5px; color: var(--muted); width: 345px; letter-spacing: .2px; }
  .required-note { position: absolute; top: 88px; font-size: 10.5px; font-weight: 600; color: var(--required); }
  .field-label { position: absolute; left: 0; font-size: 10.5px; color: var(--muted); letter-spacing: .2px; }
  .field-label .star { color: var(--required); }
  .text-field { position: absolute; left: 0; width: 298px; height: 18px; border: 1px solid var(--field-border); background: #fff; }
  .message-field { position: absolute; left: 0; top: 402px; width: 254px; height: 119px; border: 1px solid var(--field-border); background: #fff; resize: none; }
  .submit-note { position: absolute; top: 552px; width: 345px; font-size: 10.5px; line-height: 14.5px; color: var(--muted); letter-spacing: .2px; }
  .send-button { position: absolute; left: 0; top: 581px; width: 43px; height: 16px; border: 1px solid #6f7f8c;
    background: linear-gradient(#fdfdfd, #e4e8ec); font: 10.5px "Open Sans", Verdana, sans-serif; color: var(--ink); }

  .site-footer { position: absolute; left: 0; top: 873px; width: 1200px; height: 124px; background: var(--brand-orange); }
  .solutions { position: absolute; top: 6px; font-size: 18px; line-height: 22px; color: var(--footer-text); list-style: none; }
  .solutions li { padding-left: 20px; }
  .solutions li.heading { padding-left: 0; }
  .social-links { position: absolute; left: 964px; top: 8px; display: flex; gap: 10px; }
  .social-tile { width: 57px; height: 57px; border-radius: 10px; }
  .social-tile.sky { background: linear-gradient(#5cc7ef, #2a9bd1); }
  .social-tile.amber { background: linear-gradient(#ffa64a, #f07a18); }
  .social-tile.indigo { background: linear-gradient(#6d8fd3, #3b5a9f); }
  .social-reflections { position: absolute; left: 964px; top: 67px; display: flex; gap: 10px; opacity: .25; }
  .social-reflections .social-tile { height: 57px; border-radius: 10px 10px 0 0; }
</style>
</head>
<body>
  <header class="site-header">
    <div class="brand"><span class="brand-mark"></span><span class="brand-name">Harbourline Press Works</span></div>
    <div class="contact-line">Phone 000-000-0000<br>your street, your town 00000</div>
    <nav class="main-nav">
      <a href="#">Home</a><a href="#">About Us</a><a href="#">Our Products and Services</a><a href="#">FAQ</a><a href="#">Contact Us</a>
    </nav>
  </header>
  <div class="header-band"></div>

  <div class="staff-photo" role="img" aria-label="Staff portrait photo, team member in a navy company polo shirt"></div>
  <div class="partner-badge"><span class="partner-mark"></span><span class="partner-name">The Parcel Loft</span></div>
  <div class="brand-panel"><span class="brand-mark"></span><span class="brand-name">Harbourline Press Works</span></div>

  <form class="contact-form">
    <h2 class="form-title">Contact Form</h2>
    <p class="privacy-note">I respect your privacy. I will never share your email address or other information with anyone unless legally required or at your request.</p>
    <p class="required-note">* Required fields</p>
    <label class="field-label" style="top:111px">Your Name <span class="star">*</span></label>
    <input class="text-field" style="top:130px" type="text">
    <label class="field-label" style="top:156px">Your email <span class="star">*</span></label>
    <input class="text-field" style="top:176px" type="email">
    <label class="field-label" style="top:201px">Confirm email <span class="star">*</span></label>
    <input class="text-field" style="top:221px" type="email">
    <label class="field-label" style="top:246px">Your phone number</label>
    <input class="text-field" style="top:266px" type="tel">
    <label class="field-label" style="top:291px">Best time to call</label>
    <input class="text-field" style="top:311px" type="text">
    <label class="field-label" style="top:336px">Name of organization</label>
    <input class="text-field" style="top:356px" type="text">
    <label class="field-label" style="top:381px">Message <span class="star">*</span></label>
    <textarea class="message-field"></textarea>
    <p class="submit-note">Please click the submit button only once. It may take a few moments to validate and email your data.</p>
    <button class="send-button" type="button">Send</button>
  </form>

  <footer class="site-footer">
    <ul class="solutions" style="left:16px"><li class="heading">Solutions for:</li><li>Healthcare</li><li>Small Business</li><li>High Tech</li><li>More...</li></ul>
    <ul class="solutions" style="left:176px"><li class="heading">Solutions for:</li><li>Healthcare</li><li>Small Business</li><li>High Tech</li><li>More...</li></ul>
    <ul class="solutions" style="left:331px"><li class="heading">Solutions for:</li><li>Healthcare</li><li>Small Business</li><li>High Tech</li><li>More...</li></ul>
    <div class="social-links">
      <span class="social-tile sky" aria-label="Social link"></span>
      <span class="social-tile amber" aria-label="News feed link"></span>
      <span class="social-tile indigo" aria-label="Social link"></span>
    </div>
    <div class="social-reflections" aria-hidden="true">
      <span class="social-tile indigo"></span><span class="social-tile amber"></span><span class="social-tile sky"></span>
    </div>
  </footer>
</body>
</html>
```